Graphically Innovate Corporate Christmas Card

Benevix is a charitable foundation in Ontario, Canada. We support individuals and congregations with investment, fundraising and gift planning services. We are seeking an innovation graphically design Christmas Card for 2025.
As a faith-based organization, we are hoping to incorporate elements of the Christian Christmas story in the design, but the look must be creative, corporate, and elegant. Our standards are high.
A creative brief, including content copy and brand assets have been attached.
It's important that the Benevix brand is strongly featured in the design.

```html
<!DOCTYPE html>
<html lang="en">
<head>
<meta charset="utf-8">
<title>Benevix Christmas Card 2025</title>
<link rel="stylesheet" href="https://fonts.googleapis.com/css2?family=Playfair+Display:wght@400;600;700;800;900&family=Poppins:wght@400;600;700&display=swap">
<style>
  :root {
    --stage: #b3b3b3;
    --night-deep: #050a2e;
    --night-mid: #0a1a6e;
    --night-bright: #1437c4;
    --navy: #0b1b5c;
    --ink-navy: #0d2a5a;
    --leaf-green: #8cc63f;
    --quote-green: #2f4a2a;
    --white: #ffffff;
    --paper: #f4f5f7;
    --text-dark: #1a1a1a;
    --box-line: #9a9a9a;
  }
  * { margin: 0; padding: 0; box-sizing: border-box; }
  html, body { width: 960px; height: 1200px; overflow: hidden; background: var(--stage); }
  .canvas { position: relative; width: 960px; height: 1200px; }

  /* Front cover */
  .card-front {
    position: absolute; left: 109px; top: 77px; width: 742px; height: 520px; overflow: hidden;
  }
  .night-scene {
    position: absolute; inset: 0;
    background:
      radial-gradient(ellipse 95px 75px at 548px 392px, rgba(255,226,120,0.95), rgba(245,160,90,0.7) 45%, rgba(90,90,200,0) 100%),
      radial-gradient(ellipse 300px 260px at 560px 320px, rgba(30,70,230,0.75), rgba(20,55,196,0) 100%),
      linear-gradient(180deg, var(--night-deep) 0%, var(--night-mid) 45%, #0a1660 70%, #030720 100%);
  }
  .night-ground {
    position: absolute; left: 0; right: 0; bottom: 0; height: 95px;
    background: linear-gradient(180deg, rgba(4,10,50,0.85), #02051a);
  }
  .headline { position: absolute; left: 410px; top: 50px; width: 280px; text-align: center; font-family: "Playfair Display", serif; font-weight: 700; }
  .headline-joy { display: block; color: var(--white); font-size: 88px; font-weight: 700; line-height: 1; letter-spacing: 2px; }
  .headline-to { display: block; color: var(--white); font-size: 35px; font-weight: 700; line-height: 1; margin-top: 6px; letter-spacing: 1px; }
  .headline-world { display: block; color: var(--leaf-green); font-size: 62px; font-weight: 900; line-height: 1; margin-top: 2px; }

  .brand-block { position: absolute; left: 66px; top: 404px; width: 240px; text-align: center; }
  .brand-name { display: flex; align-items: center; justify-content: center; gap: 6px; }
  .brand-dot { width: 22px; height: 22px; border-radius: 50%; border: 2px solid var(--white); }
  .brand-word { font-family: "Playfair Display", serif; font-weight: 700; font-size: 29px; color: var(--white); line-height: 1; }
  .tagline { margin-top: 6px; font-family: "Playfair Display", serif; font-size: 16px; font-weight: 600; color: var(--white); display: flex; align-items: center; justify-content: center; gap: 6px; }
  .tagline-mark { color: var(--quote-green); font-size: 34px; line-height: 0.6; font-weight: 800; }
  .tagline-mark.open { margin-top: 6px; }
  .tagline-mark.close { margin-top: 16px; }
  .site { margin-top: 2px; font-family: "Poppins", sans-serif; font-size: 10px; font-weight: 700; color: var(--white); }

  /* Inside spread */
  .card-inside { position: absolute; left: 109px; top: 639px; width: 742px; height: 520px; background: var(--navy); overflow: hidden; }
  .inside-sheet {
    position: absolute; left: 19px; top: 18px; width: 708px; height: 484px;
    background: radial-gradient(ellipse at 30% 40%, #fafbfc, var(--paper) 60%, #e9ebef);
  }
  .corner-cut { position: absolute; width: 88px; height: 88px; border-radius: 50%; background: var(--navy); }
  .corner-cut.top-right { right: -44px; top: -44px; }
  .corner-cut.bottom-left { left: -44px; bottom: -44px; }
  .frame-line { position: absolute; left: 0; top: 0; }

  .verse { position: absolute; left: 22px; top: 158px; width: 290px; text-align: center; font-family: "Poppins", sans-serif; }
  .verse-icon { display: block; margin: 0 auto 20px; }
  .verse-text { font-size: 14.5px; line-height: 17.4px; color: var(--text-dark); }
  .verse-ref { margin-top: 20px; font-size: 20px; font-weight: 600; color: var(--ink-navy); }

  .greeting-box {
    position: absolute; left: 410px; top: 132px; width: 238px; height: 213px;
    border: 1px solid var(--box-line);
    display: flex; align-items: center; justify-content: center; text-align: center;
    font-family: "Poppins", sans-serif; font-size: 14.5px; line-height: 17.4px; color: var(--text-dark);
  }
</style>
</head>
<body>
<main class="canvas">

  <section class="card-front">
    <div class="night-scene" role="img" aria-label="Starry night sky over desert hills with palm trees, wise men on camels and a glowing stable with the Holy Family in silhouette"></div>
    <div class="night-ground"></div>

    <h1 class="headline">
      <span class="headline-joy">JOY</span>
      <span class="headline-to">TO THE</span>
      <span class="headline-world">WORLD</span>
    </h1>

    <div class="brand-block">
      <div class="brand-name"><span class="brand-dot"></span><span class="brand-word">Benevix</span></div>
      <div class="tagline"><span class="tagline-mark open">“</span>Faith Fueling Giving<span class="tagline-mark close">”</span></div>
      <div class="site">www.benevix.ca</div>
    </div>
  </section>

  <section class="card-inside">
    <div class="inside-sheet">
      <div class="corner-cut top-right"></div>
      <div class="corner-cut bottom-left"></div>
      <svg class="frame-line" width="708" height="484" viewBox="0 0 708 484">
        <path d="M27 24 H643 A42 42 0 0 0 683 66 V466 H66 A42 42 0 0 0 27 423 Z" fill="none" stroke="#0b1b5c" stroke-width="1"/>
      </svg>

      <div class="verse">
        <svg class="verse-icon" width="34" height="26" viewBox="0 0 34 26" aria-hidden="true">
          <path fill="#0d2a5a" d="M8 10 C9 5 12 2 15 1 L14 0 C6 2 1 8 1 15 C1 21 4 25 8 25 C12 25 15 22 15 18 C15 14 12 11 8 10 Z"/>
          <path fill="#0d2a5a" d="M26 10 C27 5 30 2 33 1 L32 0 C24 2 19 8 19 15 C19 21 22 25 26 25 C30 25 33 22 33 18 C33 14 30 11 26 10 Z"/>
        </svg>
        <p class="verse-text">Today in the town of David<br>a Savior has been<br>born to you;<br>he is the Messiah, the Lord.</p>
        <p class="verse-ref">Luke 2:11 NIV</p>
      </div>

      <div class="greeting-box">
        <p>May the gift of God’s love<br>fill your heart with joy<br>and peace<br>throughout this<br>Christmas season and<br>the year ahead.</p>
      </div>
    </div>
  </section>

</main>
</body>
</html>
```